Business Card Design

We need a new business card design for a company based in Southlake, TX. We provide business consulting services in the information technology / services space. We like variations of the color blue, aqua, black, light tan, and white. Would like "cool" tones. The design should clearly communicate professionalism. Think outside the box - we don't want something "typical". Our company name is "Vantrell Advisory, LLC".
Updates

Thank you all for your submissions. We have seen some very creative and inspired designs. We have made a decision and will be moving forward with that design. Appreciate all of the hard work.

Industry/Entity Type

Information Technology

Contact Information for Business Card

Denise Harlow Trumbey
482 West Maple Ridge Dr.
Southlake, TX 76185

```html
<!DOCTYPE html>
<html lang="en">
<head>
<meta charset="utf-8">
<title>Vantrell Advisory, LLC – Business Card</title>
<link rel="stylesheet" href="https://fonts.googleapis.com/css2?family=Open+Sans:wght@300;400&display=swap">
<style>
  :root {
    --backdrop: #e4e6ea;
    --card-white: #fbfbfb;
    --brand-blue: #2f6fc1;
    --brand-blue-soft: #4f86c9;
    --logo-circle: #5a8ccb;
    --ink: #1a1a1a;
  }
  html, body {
    margin: 0;
    width: 1200px;
    height: 960px;
    overflow: hidden;
    background: var(--backdrop);
    font-family: "Open Sans", Arial, sans-serif;
  }
  .canvas {
    position: relative;
    width: 1200px;
    height: 960px;
  }
  .business-card {
    position: absolute;
    left: 170px;
    top: 206px;
    width: 860px;
    height: 548px;
    background: var(--card-white);
    box-shadow: 0 10px 30px rgba(0,0,0,0.18);
    overflow: hidden;
  }
  .logo-circle {
    position: absolute;
    left: 282px;
    top: 88px;
    width: 100px;
    height: 100px;
    border-radius: 50%;
    background: var(--logo-circle);
  }
  .company-name {
    position: absolute;
    left: 150px;
    top: 198px;
    margin: 0;
    font-weight: 300;
    font-size: 52px;
    letter-spacing: 1px;
    color: var(--brand-blue-soft);
    white-space: nowrap;
  }
  .person-name {
    position: absolute;
    left: 368px;
    top: 300px;
    margin: 0;
    font-weight: 400;
    font-size: 27px;
    color: var(--brand-blue);
    white-space: nowrap;
  }
  .divider {
    position: absolute;
    left: 116px;
    top: 356px;
    width: 706px;
    height: 2px;
    background: var(--brand-blue);
  }
  .address {
    position: absolute;
    left: 232px;
    top: 378px;
    display: flex;
    align-items: center;
    gap: 8px;
    font-weight: 400;
    font-size: 22px;
    color: var(--ink);
    white-space: nowrap;
  }
  .address svg { width: 22px; height: 30px; }
  .bottom-band {
    position: absolute;
    left: 0;
    bottom: 0;
    width: 100%;
    height: 78px;
    background: var(--brand-blue);
  }
</style>
</head>
<body>
  <main class="canvas">
    <section class="business-card">
      <div class="logo-circle" aria-hidden="true"></div>
      <h1 class="company-name">Vantrell Advisory, LLC</h1>
      <p class="person-name">Denise Harlow Trumbey</p>
      <div class="divider"></div>
      <p class="address">
        <svg viewBox="0 0 22 30" aria-hidden="true">
          <path d="M11 1C5.5 1 1.5 5 1.5 10.3 1.5 17 11 29 11 29s9.5-12 9.5-18.7C20.5 5 16.5 1 11 1z" fill="var(--brand-blue)"/>
          <circle cx="11" cy="10.5" r="4" fill="var(--card-white)"/>
        </svg>
        <span>482 West Maple Ridge Dr. Southlake, TX 76185</span>
      </p>
      <div class="bottom-band"></div>
    </section>
  </main>
</body>
</html>
```